business card design for a plumbing contractor

i need a double business card for a plumbing business, our initial service is residential Sewer Drain Cleaning.

Target Market(s)

other plumbing Business

Industry/Entity Type

Plumbing

Contact Information for Business Card

www.PipeworksTopNotch.example- 5173829046-

Font styles to use
Serif

Colors
ec1f27
0455a3

```html
<!DOCTYPE html>
<html lang="en">
<head>
<meta charset="utf-8">
<title>Pipeworks Top Notch – Business Card</title>
<link rel="stylesheet" href="https://fonts.googleapis.com/css2?family=Roboto+Slab:wght@400;700&display=swap">
<style>
  :root {
    --brand-red: #ec1f27;
    --brand-blue: #0455a3;
    --stone: #7b7367;
    --paper: #ffffff;
    --backdrop: #e6e6e4;
    --ink-light: #fbe3e3;
  }
  * { margin: 0; padding: 0; box-sizing: border-box; }
  html, body {
    width: 1200px; height: 997px; overflow: hidden;
    background: var(--backdrop);
    font-family: "Roboto Slab", Georgia, serif;
  }
  .canvas { position: relative; width: 1200px; height: 997px; }
  .card {
    position: absolute; width: 700px; height: 400px;
    background: var(--paper); overflow: hidden;
    box-shadow: 0 10px 30px rgba(0,0,0,.18);
  }
  .card--front { left: 110px; top: 60px; }
  .card--back { left: 390px; top: 537px; }
  .card__art { position: absolute; inset: 0; }
  .wordmark {
    position: absolute; display: flex; align-items: center; gap: 14px;
    color: var(--stone); font-weight: 700; line-height: 1;
  }
  .wordmark__dot { width: 26px; height: 26px; border-radius: 50%; background: var(--brand-red); flex: none; }
  .card--front .wordmark { left: 180px; top: 118px; font-size: 56px; }
  .card--front .wordmark__dot { width: 36px; height: 36px; }
  .card--back .wordmark { left: 170px; top: 52px; font-size: 38px; }
  .contact {
    position: absolute; left: 40px; top: 250px; color: var(--paper);
  }
  .contact__name { font-size: 23px; font-weight: 700; letter-spacing: .3px; }
  .contact__role { font-size: 15px; font-weight: 400; color: var(--ink-light); margin-top: 2px; }
  .contact__list { list-style: none; margin-top: 16px; }
  .contact__item { display: flex; align-items: center; gap: 12px; font-size: 17px; margin-bottom: 10px; }
  .contact__icon { width: 24px; height: 24px; flex: none; }
</style>
</head>
<body>
<main class="canvas">

  <section class="card card--front" aria-label="Card front">
    <svg class="card__art" viewBox="0 0 700 400" aria-hidden="true">
      <path d="M0,140 C170,250 270,370 350,400 L0,400 Z" fill="var(--brand-blue)"/>
      <path d="M0,158 C160,262 255,375 322,400 L0,400 Z" fill="var(--brand-red)"/>
      <path d="M400,0 C500,50 600,150 700,240 L700,0 Z" fill="var(--brand-blue)"/>
      <path d="M428,0 C520,48 610,140 700,220 L700,0 Z" fill="var(--brand-red)"/>
    </svg>
    <div class="wordmark">
      <span>Pipeworks<br>Top Notch</span>
      <span class="wordmark__dot"></span>
    </div>
  </section>

  <section class="card card--back" aria-label="Card back">
    <svg class="card__art" viewBox="0 0 700 400" aria-hidden="true">
      <path d="M0,218 C200,170 470,200 700,100 L700,400 L0,400 Z" fill="var(--brand-blue)"/>
      <path d="M0,236 C210,188 480,218 700,118 L700,400 L0,400 Z" fill="var(--brand-red)"/>
    </svg>
    <div class="wordmark">
      <span>Pipeworks<br>Top Notch</span>
      <span class="wordmark__dot"></span>
    </div>
    <div class="contact">
      <p class="contact__name">Maren Ellwood</p>
      <p class="contact__role">Owner / Founder</p>
      <ul class="contact__list">
        <li class="contact__item">
          <svg class="contact__icon" viewBox="0 0 24 24" aria-hidden="true">
            <circle cx="12" cy="12" r="12" fill="var(--ink-light)"/>
            <path d="M8.5 6.5c.6-.4 1.3-.2 1.6.4l1 2c.2.5.1 1-.3 1.3l-.8.6c.6 1.3 1.6 2.4 2.9 3l.6-.8c.3-.4.9-.5 1.3-.3l2 1c.6.3.8 1 .4 1.6-.8 1.3-2.2 1.8-3.6 1.2-3-1.2-5.1-3.4-6.3-6.3-.5-1.4 0-2.9 1.2-3.7z" fill="var(--brand-red)"/>
          </svg>
          <span>5173829046</span>
        </li>
        <li class="contact__item">
          <svg class="contact__icon" viewBox="0 0 24 24" aria-hidden="true">
            <circle cx="12" cy="12" r="12" fill="var(--ink-light)"/>
            <g fill="none" stroke="var(--brand-red)" stroke-width="1.3">
              <circle cx="12" cy="12" r="6"/>
              <ellipse cx="12" cy="12" rx="2.6" ry="6"/>
              <path d="M6 12h12"/>
            </g>
          </svg>
          <span>www.PipeworksTopNotch.example</span>
        </li>
      </ul>
    </div>
  </section>

</main>
</body>
</html>
```